Electrical Wholesaler Needs a New Website

Looking for a new website to be built for an electrical wholesaler based in Birmingham(England). Our logo is based on two Lions with a shield, so ideally the site should be deigned around that.

Looking for something that shows off our logo and incorporates what we are trying to do, preferably to have a colour scheme that is green and black if possible.

Target Market(s)

I'm looking for a professional website for my company that doesn't just look like amother WordPress template that I could build myself.

Industry/Entity Type

Electrical

Font styles to use
Sans Serif

Colors
9bcb3c
cadf82

Requirements
Must have
• Website with 4-5 pages, home page, about us, suppliers list, catalogue download and contact us. Search for UK electrical wholesalers to give you an idea of what I mean.

```html
<!DOCTYPE html>
<html lang="en">
<head>
<meta charset="utf-8">
<title>Ashgrove Electrical Wholesalers</title>
<link rel="stylesheet" href="https://fonts.googleapis.com/css2?family=Habibi&family=Open+Sans:ital,wght@1,400&display=swap">
<style>
:root{
  --lime:#9bcb3c;
  --lime-pale:#cadf82;
  --green-deep:#1f4a34;
  --green-dark:#123524;
  --green-text:#6a9a1c;
  --green-title:#2c5a3a;
  --ink:#3a3a3a;
  --body-text:#777;
  --line:#d9d9d9;
  --footer:#2b2b2b;
  --white:#fff;
}
*{box-sizing:border-box;margin:0;padding:0}
html,body{width:1120px;height:1200px;overflow:hidden}
body{
  position:relative;
  background:linear-gradient(180deg,var(--lime) 0%,var(--lime-pale) 100%);
  font-family:"Habibi",Georgia,serif;
  color:var(--ink);
}
.page{position:absolute;left:112px;top:0;width:896px;height:1200px;background:var(--white)}
.abs{position:absolute}

.brand{left:14px;top:34px;display:flex;align-items:center;gap:8px}
.brand-mark{width:18px;height:18px;background:var(--green-deep)}
.brand-name{font-size:20px;color:var(--green-deep);line-height:1.1;width:150px}

.contact-phone{right:8px;top:12px;display:flex;align-items:center;gap:10px;font-size:22px;color:var(--green-text);letter-spacing:1px}
.contact-mail{right:20px;top:49px;display:flex;align-items:center;gap:14px;font-family:"Open Sans",Arial,sans-serif;font-style:italic;font-size:13px;color:#555}
.search{left:652px;top:84px;width:235px;height:32px;border:1px solid var(--line);border-radius:3px;
  font-family:"Open Sans",Arial,sans-serif;font-style:italic;font-size:12px;color:#aaa;padding:8px 11px}
.search-btn{position:absolute;right:0;top:5px;width:36px;height:20px;border-left:1px solid var(--line);display:flex;justify-content:center}

.nav{left:8px;top:131px;width:880px;height:44px;border-radius:3px;
  background:linear-gradient(180deg,#2e6247 0%,var(--green-dark) 100%);
  display:flex;align-items:center;padding-left:19px}
.nav a{color:var(--white);text-decoration:none;font-size:13px;padding:0 25px;border-left:1px solid #3d7458;line-height:22px}
.nav a:first-child{border-left:none;padding-left:9px}

.slider{left:9px;top:182px;width:878px;height:328px;border-radius:3px;
  background:linear-gradient(100deg,#e8e4d8 0%,#f1f0ec 45%,#e9ebe9 100%);box-shadow:0 3px 4px #ccc}
.slide-caption{left:364px;top:79px;width:405px;min-height:175px;background:rgba(70,70,70,.82);color:var(--white);padding:12px 18px 18px}
.slide-caption h1{font-weight:400;font-size:31px;line-height:42px;white-space:nowrap;letter-spacing:-.3px}
.slide-caption p{font-size:11.5px;line-height:19.5px;margin-top:10px;padding-left:2px}
.slide-arrow{top:131px;width:26px;height:44px;background:var(--white);display:flex;align-items:center;justify-content:center;border-radius:2px}

.bar{border:1px solid var(--line);height:39px;background:linear-gradient(180deg,#fff,#f3f3f3);font-size:20px;color:#555;padding:7px 19px}
.featured{left:8px;top:565px;width:880px}
.pager{position:absolute;right:10px;top:9px;display:flex;gap:3px}
.pager span{width:19px;height:19px;border-radius:50%;background:linear-gradient(#bbb,#888);display:flex;align-items:center;justify-content:center}

.product{top:623px;width:206px;height:141px}
.product-label{position:absolute;left:0;bottom:0;width:100%;height:42px;background:rgba(110,110,110,.78);color:var(--white);font-size:19px;padding:9px 16px}

.welcome-bar{left:8px;top:816px;width:656px}
.welcome{left:15px;top:876px;width:650px;font-size:11.4px;line-height:19.6px;color:var(--body-text)}
.welcome p+p{margin-top:21px}
.read-more{display:block;margin-top:18px;color:var(--green-text);text-decoration:none}

.deals-bar{left:680px;top:816px;width:208px;color:var(--green-title);padding-left:13px}
.deal{left:679px;top:866px;width:209px;height:210px;border:1px solid var(--line);background:#f8f8f8}
.deal-photo{height:121px;background:linear-gradient(135deg,#6a5a40,#c4411f 50%,#3d4a8a)}
.deal h3{font-weight:400;font-size:15px;color:var(--green-text);margin:10px 0 0 11px;white-space:nowrap}
.deal p{font-size:12px;line-height:17px;color:#666;margin:9px 10px 0 12px}
.deal a{color:var(--green-text);font-size:11px;text-decoration:none;margin-left:4px}

.footer{left:0;top:1111px;width:896px;height:89px;background:var(--footer);color:#ddd;font-size:12px}
.footer-links{position:absolute;left:18px;top:21px}
.footer-copy{position:absolute;left:18px;top:50px}
.social{position:absolute;right:27px;top:32px;display:flex;gap:5px}
.social span{width:26px;height:26px;border-radius:50%;background:#a5a5a5;display:flex;align-items:center;justify-content:center}
</style>
</head>
<body>
<div class="page">
  <div class="abs brand"><span class="brand-mark"></span><span class="brand-name">Ashgrove Electrical Wholesalers</span></div>

  <div class="abs contact-phone">
    <svg width="18" height="18" viewBox="0 0 18 18"><rect width="18" height="18" rx="3" fill="#bbb"/><path d="M6 4h2l1 3-1.5 1a6 6 0 0 0 2.5 2.5L11 9l3 1v2c0 1-1 2-2 2A9 9 0 0 1 4 6c0-1 1-2 2-2z" fill="#fff"/></svg>
    <span>0121 555 0147</span>
  </div>
  <div class="abs contact-mail">
    <svg width="22" height="14" viewBox="0 0 22 14"><rect width="22" height="14" fill="#c8c8c8"/><path d="M0 0l11 8 11-8" stroke="#fff" fill="none"/></svg>
    <span>sales@ashgrove-elec.co.uk</span>
  </div>
  <div class="abs search">Search here...
    <span class="search-btn"><svg width="20" height="20" viewBox="0 0 20 20"><circle cx="8" cy="8" r="6" stroke="#333" stroke-width="2" fill="none"/><path d="M12 12l6 6" stroke="#333" stroke-width="3"/></svg></span>
  </div>

  <nav class="abs nav">
    <a href="#">HOME</a><a href="#">ABOUT US</a><a href="#">SERVICES</a><a href="#">GALLERY</a><a href="#">BLOG</a><a href="#">TESTIMONIALS</a><a href="#">CONTACT US</a>
  </nav>

  <div class="abs slider" role="img" aria-label="Yellow multimeter with test leads, wall switch and rolled blueprints">
    <div class="abs slide-caption">
      <h1>All your Electrical Need</h1>
      <p>Lorem ipsum dolor sit amet, consectetur adipisicing elit, sed do eiusmod tempor incididunt ut labore et dolore magna aliqua. Ut enim ad minim veniam, quis nostrud exercitation ullamco laboris nisi ut aliquip ex ea commodo consequat.</p>
    </div>
    <div class="abs slide-arrow" style="left:2px"><svg width="8" height="14"><path d="M7 1L1 7l6 6" stroke="#888" fill="none"/></svg></div>
    <div class="abs slide-arrow" style="right:2px"><svg width="8" height="14"><path d="M1 1l6 6-6 6" stroke="#888" fill="none"/></svg></div>
  </div>

  <div class="abs bar featured">Featured Products
    <div class="pager">
      <span><svg width="6" height="10"><path d="M5 1L1 5l4 4" stroke="#fff" stroke-width="2" fill="none"/></svg></span>
      <span><svg width="6" height="10"><path d="M1 1l4 4-4 4" stroke="#fff" stroke-width="2" fill="none"/></svg></span>
    </div>
  </div>

  <div class="abs product" style="left:9px;background:linear-gradient(135deg,#c9c0b0,#ece6dc)" role="img" aria-label="Chrome downlight and energy saving lamp"><div class="product-label">LAMPS DESIGN</div></div>
  <div class="abs product" style="left:233px;background:linear-gradient(135deg,#8a8a8a,#dcdcdc)" role="img" aria-label="Metal wall switch plate"><div class="product-label">SWITCH GEARS</div></div>
  <div class="abs product" style="left:457px;background:linear-gradient(135deg,#9a9a9a,#e0dcc8)" role="img" aria-label="Reels of grey and green-yellow cable"><div class="product-label">CABEL WIRES</div></div>
  <div class="abs product" style="left:680px;background:linear-gradient(135deg,#f2f2f2,#444)" role="img" aria-label="White and black flexible ventilation ducting"><div class="product-label">VENTILATION</div></div>

  <div class="abs bar welcome-bar">Welcome to Our Site...</div>
  <div class="abs welcome">
    <p>Lorem ipsum dolor sit amet, consectetur adipisicing elit, sed do eiusmod tempor incididunt ut labore et dolore magna aliqua. Ut enim ad minim veniam, quis nostrud exercitation ullamco laboris nisi ut aliquip ex ea commodo consequat. Duis aute irure dolor in reprehenderit in voluptate velit esse cillum dolore eu fugiat nulla pariatur.</p>
    <p>Excepteur sint occaecat cupidatat non proident, sunt in culpa qui officia deserunt mollit anim id est laborum. Nam libero tempore, cum soluta nobis est eligendi optio cumque nihil impedit quo minus id quod maxime placeat facere possimus, omnis voluptas assumenda est, omnis dolor repellendus. Temporibus autem quibusdam et aut officiis debitis aut rerum necessitatibus saepe eveniet ut et voluptates repudiandae sint et molestiae non recusandae.</p>
    <a class="read-more" href="#">Read More &gt;&gt;</a>
  </div>

  <div class="abs bar deals-bar">Special Deals</div>
  <div class="abs deal">
    <div class="deal-photo" role="img" aria-label="Pliers, screwdrivers and a voltage tester on a workbench"></div>
    <h3>Tools &amp; Test Equipments</h3>
    <p>Temporibus autem quibusdam et aut officiis debitis <a href="#">more &gt;&gt;</a></p>
  </div>

  <footer class="abs footer">
    <div class="footer-links">Terms &amp; Conditions | Legal Info | Privacy Statement</div>
    <div class="footer-copy">© 2013 ashgrove All Rights Reserved</div>
    <div class="social">
      <span></span><span></span>
      <span><svg width="12" height="12"><path d="M6 1v10M1 6h10" stroke="#fff" stroke-width="2.5"/></svg></span>
      <span><svg width="12" height="12"><circle cx="2" cy="10" r="1.6" fill="#fff"/><path d="M1 5a6 6 0 0 1 6 6M1 1a10 10 0 0 1 10 10" stroke="#fff" stroke-width="2" fill="none"/></svg></span>
    </div>
  </footer>
</div>
</body>
</html>
```